Quill Builds Needs a Website!

Single page (plus contact form) website for small home remodeling company. He's got a few pictures he'd like on the site and needs some basic text. He likes clean, simple designs and is "more traditional" in his stylistic preferences. Most of his business comes from word-of-mouth advertising and so the site is just something he needs for people to feel more comfortable with his business.
Updates

Target Market(s)

People who want to remodel their homes

Coding

Coded - Design and coding required

Number of Pages Required

2 page

Requirements
Must have
• Main page to include some or all of the attached images, contact page. Neutral colors. Old domain: brindlecoveroofing.com New domain: mq-outfitters.com You can pull text from the old site or update it.
Should not have
• No loud colors/loud visual elements

```html
<!DOCTYPE html>
<html lang="en">
<head>
<meta charset="utf-8">
<title>Martin Quill Enterprises – Quill Builds</title>
<link href="https://fonts.googleapis.com/css2?family=Montserrat:wght@400;500;600;700;800&display=swap" rel="stylesheet">
<style>
:root{
  --brown:#3b1410;
  --brown-deep:#2c0f0c;
  --orange:#e07b2a;
  --ink:#1d1d1d;
  --muted:#5b5b5b;
  --light:#f7f7f7;
  --white:#ffffff;
}
*{margin:0;padding:0;box-sizing:border-box}
html,body{width:1200px;height:3552px;overflow:hidden;background:var(--white)}
body{position:relative;font-family:'Montserrat',sans-serif;color:var(--ink)}
.abs{position:absolute}
.center{text-align:center}

/* header */
.brand-box{left:0;top:0;width:244px;height:64px;background:var(--brown);display:flex;align-items:center;gap:18px;padding-left:26px}
.brand-box .dot{width:30px;height:30px;border-radius:50%;background:var(--orange);flex:none}
.brand-box .name{color:var(--white);font-weight:800;font-size:16px;line-height:19px;text-align:center}
.nav{top:25px;font-size:12px;color:var(--ink)}
.nav.active{color:var(--orange);border-bottom:1px solid var(--orange);padding-bottom:2px}
.social-dot{width:19px;height:19px;border-radius:50%;border:1px solid #bbb;top:24px}
.call-box{left:989px;top:0;width:211px;height:73px;background:var(--orange);color:var(--white);font-weight:700;text-align:center;padding-top:12px}
.call-box .l1{font-size:15px;letter-spacing:.5px}
.call-box .l2{font-size:17px;letter-spacing:2px;margin-top:6px}

/* hero */
.hero{left:0;top:73px;width:1200px;height:585px;background:linear-gradient(160deg,#5a4638 0%,#3e2e25 45%,#6a5848 75%,#4a3a30 100%)}
.hero-title{left:0;top:232px;width:1200px;color:var(--white);font-weight:800;font-size:84px;line-height:92px;text-shadow:0 2px 6px rgba(0,0,0,.3)}
.btn{background:var(--orange);color:var(--white);display:flex;align-items:center;justify-content:center;font-size:11.5px;letter-spacing:.5px}
.hero-btn{left:477px;top:467px;width:244px;height:47px;font-size:15px}

/* about */
.about-shadow{left:125px;top:814px;width:416px;height:269px;background:var(--brown)}
.about-photo{left:98px;top:779px;width:425px;height:284px;background:linear-gradient(135deg,#c9b89c,#8a7a68 55%,#d8d0c4)}
.h2{font-weight:600;font-size:30px;color:var(--ink)}
.about-title{left:601px;top:800px}
.about-title::after{content:"";display:block;width:96px;height:2px;background:var(--orange);margin-top:2px}
.about-text{left:601px;top:853px;width:470px;font-size:13.5px;line-height:23.3px;color:var(--muted)}
.about-btn{left:601px;top:1047px;width:141px;height:33px}

/* band */
.band{left:0;top:1204px;width:1198px;height:587px;background:var(--brown)}
.band-title{left:0;top:1244px;width:1198px;color:var(--white);font-weight:600;font-size:30px}
.band-rule{left:506px;top:1298px;width:185px;height:2px;background:var(--white)}
.card{top:1386px;width:264px;height:320px;background:var(--white)}
.tag{left:-12px;top:13px;width:154px;height:49px;background:var(--orange);border-radius:0 25px 25px 0;color:var(--white);font-size:13.5px;display:flex;align-items:center;padding-left:22px}
.tag::before{content:"";position:absolute;left:0;bottom:-10px;width:12px;height:10px;background:#9a4e14;clip-path:polygon(0 0,100% 0,100% 100%)}
.card-icon{left:102px;top:82px;width:60px;height:60px;border:1.5px solid var(--orange);border-radius:8px;background:#fbeee2}
.card-text{left:14px;top:162px;width:236px;font-size:13.5px;line-height:24px;color:var(--ink);text-align:center}
.card-link{left:29px;top:260px;font-size:12px;color:var(--orange)}
.corner{right:-11px;bottom:-5px;width:84px;height:76px;background:var(--orange);clip-path:polygon(100% 0,100% 100%,0 100%)}
.corner-num{right:12px;bottom:6px;color:var(--white);font-size:30px;font-weight:400}

/* blog */
.section-title{font-weight:600;font-size:30px}
.rule{height:3px;background:var(--brown)}
.post-img{top:1995px;height:203px}
.post-date{top:2214px;font-size:10px;color:var(--ink)}
.post-title{top:2240px;font-size:15px;color:var(--ink)}
.post-text{top:2280px;font-size:11.5px;line-height:14.5px;color:var(--muted)}
.post-link{top:2381px;font-size:11px;letter-spacing:1px;color:var(--ink)}

/* testimonials */
.testi-bg{left:0;top:2541px;width:1200px;height:606px;background:var(--light)}
.t-card{top:2664px;height:380px;background:var(--white);box-shadow:0 2px 12px rgba(0,0,0,.06)}
.avatar{top:20px;width:91px;height:91px;border-radius:50%;background:#d6d6d6}
.quote{font-size:12px;line-height:18.5px;color:var(--ink);text-align:center}
.stars{color:var(--orange);font-size:24px;letter-spacing:2px}
.t-name{font-size:13px;color:var(--ink)}

/* footer */
.footer{left:0;top:3147px;width:1200px;height:405px;background:var(--brown)}
.f-brand{left:65px;top:3237px;color:var(--white);font-weight:600;font-size:30px}
.f-text{left:65px;top:3294px;width:240px;color:var(--white);font-size:13.5px;line-height:21px}
.f-social{top:3416px;width:18px;height:18px;border-radius:50%;border:1.5px solid var(--white)}
.f-head{color:var(--white);font-size:22px;top:3246px}
.f-list{list-style:none;color:var(--white);font-size:13.5px}
.f-list li{position:relative;padding-left:32px}
.f-list li::before{content:"";position:absolute;left:0;top:7px;width:7px;height:7px;border-radius:50%;background:var(--orange)}
.f-call{left:858px;top:3240px;color:var(--white);font-size:24px}
.f-phone{left:858px;top:3278px;color:var(--orange);font-size:24px}
.f-contact{left:860px;color:var(--white);font-size:23px;display:flex;align-items:center;gap:30px}
.f-rule{left:65px;top:3503px;width:1077px;height:1px;background:#8a6a66}
.f-copy{left:0;top:3518px;width:1200px;color:var(--white);font-size:15px;text-align:center}
</style>
</head>
<body>

<!-- Header -->
<div class="abs brand-box"><span class="dot"></span><span class="name">Quill<br>Builds</span></div>
<span class="abs nav active" style="left:285px">Home</span>
<span class="abs nav" style="left:361px">Services</span>
<span class="abs nav" style="left:454px;line-height:13px">Project<br>s</span>
<span class="abs nav" style="left:545px">Blogs</span>
<span class="abs nav" style="left:617px">About us</span>
<span class="abs nav" style="left:714px;line-height:13px">Contacts<br>us</span>
<span class="abs social-dot" style="left:840px" aria-label="Social link"></span>
<span class="abs social-dot" style="left:873px" aria-label="Social link"></span>
<span class="abs social-dot" style="left:906px" aria-label="Social link"></span>
<span class="abs social-dot" style="left:939px" aria-label="Social link"></span>
<div class="abs call-box"><div class="l1">CALL US TODAY !</div><div class="l2">555-014-2870</div></div>

<!-- Hero -->
<div class="abs hero" role="img" aria-label="Bright home office interior with shelving, desk and plants by the windows"></div>
<h1 class="abs hero-title center">Martin Quill<br>Enterprises</h1>
<div class="abs btn hero-btn">MAKE AN APPOINMENTS</div>

<!-- About -->
<div class="abs about-shadow"></div>
<div class="abs about-photo" role="img" aria-label="Remodeled living room with staircase, sofa and kitchen bar"></div>
<h2 class="abs h2 about-title">ABOUT US</h2>
<p class="abs about-text">When you want affordable, quality home construction services; think of us to do the job.<br>Since 1981 Martin Quill has built and remodeled over 400 homes and businesses. Let us be your contractor for the next project you start.<br>When quality, value and personal attention to detail are important<br>With over 20 years experience in residential and commercial construction, you can trust your project to Brindle Cove Homes</p>
<div class="abs btn about-btn">LEARN MORE</div>

<!-- Band -->
<div class="abs band"></div>
<h2 class="abs band-title center">DON'T TINKER AROUND</h2>
<div class="abs band-rule"></div>

<div class="abs card" style="left:95px">
  <div class="abs tag">PARTNERSHIP</div>
  <div class="abs card-icon" role="img" aria-label="Handshake icon"></div>
  <p class="abs card-text">I Have Built My Business With A Partnership Of Clients, Employees, Subcontractors</p>
  <span class="abs card-link">LEARN MORE</span>
  <div class="abs corner"></div><span class="abs corner-num">1</span>
</div>
<div class="abs card" style="left:477px">
  <div class="abs tag">CONSTRUCTION</div>
  <div class="abs card-icon" role="img" aria-label="House with tools icon"></div>
  <p class="abs card-text">I Have Deep "Hands On" History In Construction From Foundations To Final Finishing Touches.</p>
  <span class="abs card-link">LEARN MORE</span>
  <div class="abs corner"></div><span class="abs corner-num">2</span>
</div>
<div class="abs card" style="left:859px">
  <div class="abs tag">SUPPLIER</div>
  <div class="abs card-icon" role="img" aria-label="Supplier with boxes icon"></div>
  <p class="abs card-text">We Cultivate Suppliers Who Deliver Quality Materials On Time And Without Damage.</p>
  <span class="abs card-link">LEARN MORE</span>
  <div class="abs corner"></div><span class="abs corner-num">3</span>
</div>

<!-- Blog -->
<h2 class="abs section-title center" style="left:0;top:1880px;width:1188px">OUR BLOG</h2>
<div class="abs rule" style="left:543px;top:1927px;width:100px"></div>

<div class="abs post-img" style="left:94px;width:271px;background:linear-gradient(135deg,#6d6e6a,#9a9a92 50%,#4e4a44)" role="img" aria-label="Bathroom with glass shower and soaking tub"></div>
<div class="abs post-img" style="left:437px;width:298px;background:linear-gradient(135deg,#c9b89c,#8a7a68 55%,#d8d0c4)" role="img" aria-label="Living room with staircase and blue accents"></div>
<div class="abs post-img" style="left:792px;width:299px;top:1998px;height:200px;background:linear-gradient(135deg,#24487a,#8b857c 45%,#4b3526)" role="img" aria-label="Kitchen with steel fridge and dark wood cabinets"></div>

<div class="abs post-date center" style="left:94px;width:271px">28 /09 /2020</div>
<div class="abs post-title center" style="left:94px;width:271px">Small Bathroom Ideas</div>
<p class="abs post-text center" style="left:110px;width:240px">sed ut perspiciatis, unde omnis iste natus error sit voluptatem accusantium doloremque laudantium, totam rem aperiam eaque ipsa, quae ab illo inventore veritatis et quasi architecto</p>
<div class="abs post-link center" style="left:94px;width:292px">READ FULL ARTICLE</div>

<div class="abs post-date center" style="left:437px;width:298px">28 /09 /2020</div>
<div class="abs post-title center" style="left:437px;width:316px">Elegant Floating Vanities</div>
<p class="abs post-text center" style="left:466px;width:240px">sed ut perspiciatis, unde omnis iste natus error sit voluptatem accusantium doloremque laudantium, totam rem aperiam eaque ipsa, quae ab illo inventore veritatis et quasi architecto</p>
<div class="abs post-link center" style="left:437px;width:320px">READ FULL ARTICLE</div>

<div class="abs post-date center" style="left:792px;width:299px">28 /09 /2020</div>
<div class="abs post-title center" style="left:792px;width:312px">Small Bathroom Ideas</div>
<p class="abs post-text center" style="left:825px;width:252px">sed ut perspiciatis, unde omnis iste natus error sit voluptatem accusantium doloremque laudantium, totam rem aperiam eaque ipsa, quae ab illo inventore veritatis et quasi architecto</p>
<div class="abs post-link center" style="left:792px;width:332px">READ FULL ARTICLE</div>

<div class="abs btn" style="left:520px;top:2438px;width:142px;height:33px">LEARN MORE</div>

<!-- Testimonials -->
<div class="abs testi-bg"></div>
<h2 class="abs section-title center" style="left:0;top:2594px;width:1196px">TESTIMONIAL</h2>
<div class="abs rule" style="left:547px;top:2640px;width:102px;background:var(--orange);height:2px"></div>

<div class="abs t-card" style="left:120px;width:418px">
  <div class="abs avatar" style="left:163px" role="img" aria-label="Customer avatar placeholder"></div>
  <p class="abs quote" style="left:24px;top:134px;width:370px">“Martin updated our ' 92 kitchen – a complex job involving tearing out a brick wall and re-configuring it with a pantry, buffet and large appliance garages. Martin was VERY patient as I struggled with design ideas. He has expert craftsmen; visits every day to check the work; a great communicator; budget-conscious (talked us into keeping and painting the old cabinets and they are beautiful), and he is now the best friend of our unfriendly dog. The result is beautiful, and the price was right. ”</p>
  <div class="abs stars center" style="left:0;top:318px;width:418px">★★★★★</div>
  <div class="abs t-name center" style="left:0;top:355px;width:418px">- DANA R</div>
</div>

<div class="abs t-card" style="left:656px;width:420px;height:378px">
  <div class="abs avatar" style="left:164px" role="img" aria-label="Customer avatar placeholder"></div>
  <p class="abs quote" style="left:100px;top:166px;width:220px">“Martin Quill doesn't always tell you what you want to hear, but he does tell you the truth.”</p>
  <div class="abs stars center" style="left:0;top:310px;width:420px">★★★★★</div>
  <div class="abs t-name center" style="left:0;top:348px;width:420px">- COREY M.</div>
</div>

<div class="abs btn" style="left:527px;top:3081px;width:141px;height:33px">LEARN MORE</div>

<!-- Footer -->
<div class="abs footer"></div>
<div class="abs f-brand">Brindle Cove</div>
<p class="abs f-text">Since 1981 Martin Quill has built and remodeled over 400 homes and businesses. Let us be your contractor for the next project you start.</p>
<span class="abs f-social" style="left:73px" aria-label="Social link"></span>
<span class="abs f-social" style="left:124px" aria-label="Social link"></span>
<span class="abs f-social" style="left:179px" aria-label="Social link"></span>
<span class="abs f-social" style="left:225px" aria-label="Social link"></span>

<div class="abs f-head" style="left:361px">SERVICE</div>
<ul class="abs f-list" style="left:361px;top:3287px;line-height:23.5px">
  <li>Addition</li><li>New Construction</li><li>historic renovations</li><li>painting</li><li>gutters</li><li>electric</li>
</ul>

<div class="abs f-head" style="left:598px;top:3242px">CUSTOMER CARE</div>
<ul class="abs f-list" style="left:598px;top:3283px;line-height:30px">
  <li>About Us</li><li>Our Services</li><li>blog</li><li>Contact Us</li><li>Contact Us</li>
</ul>

<div class="abs f-call">Call Now For Services!</div>
<div class="abs f-phone">555-014-2870</div>
<div class="abs f-contact" style="top:3336px">
  <svg width="22" height="16" viewBox="0 0 22 16" fill="none" stroke="#fff" stroke-width="1.4"><rect x="1" y="1" width="20" height="14"/><path d="M1 1l10 8 10-8"/></svg>
  <span>Email Us</span>
</div>
<div class="abs f-contact" style="top:3390px">
  <svg width="22" height="26" viewBox="0 0 22 26" fill="none" stroke="#fff" stroke-width="1.4"><path d="M11 25s9-9 9-15a9 9 0 0 0-18 0c0 6 9 15 9 15z"/><circle cx="11" cy="10" r="3.2"/></svg>
  <span>Get Direction</span>
</div>
<div class="abs f-rule"></div>
<div class="abs f-copy">Brindle Cove © 2021 All Rights Reserved. Terms of Use and Privacy Policy</div>

</body>
</html>
```